Start up business website

IT Support provider that caters towards law enforcement / police departments. We'll offer remote IT support, backup / recovery services and cyber security. Will add updates soon.

Target Market(s)

Police departments / Law Enforcement

Coding

Coded - Design and coding required

Number of Pages Required

5+ page

Font styles to use
Other font styles liked:
• Use font style in uploaded logo

Colors
0054AA
0677BA
7BADD7
CADEEF
E8F1F8

```html
<!DOCTYPE html>
<html lang="en">
<head>
<meta charset="utf-8">
<title>Bulwark Support</title>
<link href="https://fonts.googleapis.com/css2?family=Orbitron:wght@700;900&family=Poppins:wght@400;500;600;700&display=swap" rel="stylesheet">
<style>
:root{
  --blue:#0054AA;--blue-mid:#0677BA;--blue-soft:#7BADD7;--blue-pale:#CADEEF;--blue-ice:#E8F1F8;
  --ink:#1d1f24;--text:#6a6e76;--dark:#1c1f26;--grey:#eeeeee;--white:#fff;
}
*{margin:0;padding:0;box-sizing:border-box}
html,body{width:1200px;height:4504px;overflow:hidden}
body{position:relative;font-family:'Poppins',sans-serif;color:var(--text);background:var(--white)}
.abs{position:absolute}
.display{font-family:'Orbitron',sans-serif;font-weight:900;letter-spacing:4px;color:var(--ink);text-transform:uppercase}
.para{font-size:15px;line-height:26px}
.btn{display:inline-block;background:var(--blue);color:#fff;font-size:12px;font-weight:600;padding:12px 22px;text-transform:uppercase}
/* header */
.topbar{top:0;left:0;width:1200px;height:34px;display:flex;justify-content:flex-end;align-items:center;gap:22px;padding-right:150px;font-size:12px;color:var(--ink)}
.topbar .contact{display:flex;align-items:center;gap:8px}
.topbar .dot{width:18px;height:18px;border-radius:50%;background:var(--blue)}
.social{display:flex;gap:10px}
.social span{width:22px;height:22px;border-radius:50%;background:var(--blue)}
.brand{top:22px;left:88px;display:flex;align-items:center;gap:10px}
.brand .mark{width:46px;height:46px;background:var(--blue)}
.brand b{font-family:'Orbitron',sans-serif;font-weight:900;font-size:26px;color:var(--blue);letter-spacing:1px}
.nav{top:62px;left:405px;display:flex;gap:30px;font-size:13px;font-weight:500;color:var(--ink);text-transform:uppercase}
.nav-cta{top:52px;left:968px;background:#e4e4e4;color:var(--ink);font-size:13px;font-weight:600;padding:10px 22px;text-transform:uppercase}
/* hero */
.hero-photo{top:128px;left:0;width:1200px;height:800px;background:linear-gradient(100deg,#121518 0%,#2a3038 45%,#3d444c 70%,#1e2228 100%)}
.hero-title{top:345px;left:88px;font-size:66px;line-height:72px;color:#fff;letter-spacing:6px}
.hero-sub{top:492px;left:90px;color:#fff;font-size:13px;font-weight:600;text-transform:uppercase}
.hero-btn{top:520px;left:90px;background:#fff;color:var(--ink)}
/* tabs */
.tabs{top:1010px;left:90px;width:1020px;display:flex;justify-content:space-around;font-size:14px;color:var(--ink);text-transform:uppercase;border-bottom:2px solid var(--grey);padding-bottom:14px}
.tabs .active{color:var(--blue);position:relative}
.tabs .active::after{content:"";position:absolute;left:-40px;right:-40px;bottom:-16px;height:3px;background:var(--blue)}
/* cards */
.card{background:#fff;box-shadow:0 10px 40px rgba(0,0,0,.12)}
.photo{background:linear-gradient(160deg,#6b7480,#2f3a48)}
.dots{width:64px;height:48px;background-image:radial-gradient(var(--ink) 2.5px,transparent 3px);background-size:16px 16px}
/* about */
.about-title{top:1850px;left:90px;font-size:36px;color:#fff}
.about-text{top:1910px;left:90px;width:440px;color:#fff}
.cjis-label{top:1855px;left:622px;font-family:'Orbitron',sans-serif;font-weight:700;font-size:20px;color:#fff;letter-spacing:1px}
.service{top:1900px;width:180px;height:244px;display:flex;flex-direction:column;align-items:center;justify-content:center;gap:22px;text-align:center;font-size:13px;font-weight:700;color:var(--ink);text-transform:uppercase;line-height:20px}
.arrow-btn{top:2188px;width:32px;height:32px;border:1px solid #fff;display:flex;align-items:center;justify-content:center}
/* testimonials */
.quote{top:3440px;width:330px;height:210px;padding:30px 30px 0}
.quote .avatar{position:absolute;top:-40px;left:30px;width:78px;height:78px;border-radius:50%;border:4px solid #fff;background:linear-gradient(135deg,#c9a98f,#6b4b3a)}
.quote p{margin-top:28px;font-size:14px;line-height:24px}
.quote .meta{position:absolute;left:30px;right:30px;bottom:18px;display:flex;justify-content:space-between;border-top:1px solid var(--grey);padding-top:14px;font-size:13px;font-weight:700;color:var(--ink);text-transform:uppercase}
.stars{color:#f4b400;letter-spacing:2px}
/* footer */
.footer{top:3940px;left:0;width:1200px;height:564px;background:var(--dark);color:#c9ccd2}
.news-title{top:4000px;left:0;width:1200px;text-align:center;font-size:40px;color:#fff}
.news-form{top:4060px;left:340px;display:flex}
.news-form span{width:400px;height:44px;background:#fff;color:#777;font-size:13px;padding:12px 18px}
.news-form b{width:120px;height:44px;background:var(--blue);color:#fff;font-size:13px;display:flex;align-items:center;justify-content:center}
.col{top:4176px;font-size:13px;line-height:25px}
.col h4{color:#fff;font-size:15px;text-transform:uppercase;margin-bottom:10px}
.col li{list-style:none}
.col li::before{content:"› ";color:var(--blue-soft)}
.copy{top:4436px;left:0;width:1200px;text-align:center;font-size:12px;color:#fff;text-transform:uppercase;border-top:1px solid #33373f;padding-top:20px}
</style>
</head>
<body>

<header>
  <div class="abs topbar">
    <div class="contact"><span class="dot"></span>+00 (00) 456 789</div>
    <div class="contact"><span class="dot"></span>info@example.com</div>
    <div class="social"><span></span><span></span><span></span></div>
  </div>
  <div class="abs brand"><span class="mark"></span><b>BULWARK</b></div>
  <nav class="abs nav"><span>Home</span><span>Services</span><span>Follow Up</span><span>CJIS Compliance</span><span>Contact Us</span></nav>
  <div class="abs nav-cta">Get in Touch</div>
</header>

<section>
  <div class="abs hero-photo" role="img" aria-label="Row of police officers in uniform on a city street at night"></div>
  <svg class="abs" style="top:760px;left:0" width="1200" height="170" viewBox="0 0 1200 170">
    <polygon points="0,140 600,30 1200,120 1200,170 0,170" fill="#7BADD7"/>
    <polygon points="0,160 600,50 1200,140 1200,170 0,170" fill="#fff"/>
  </svg>
  <h1 class="abs display hero-title">Bulwark<br>Support</h1>
  <div class="abs hero-sub">Public safety promotional training, selection &amp; more</div>
  <div class="abs btn hero-btn">Visit our online store now!</div>
</section>

<div class="abs tabs"><span class="active">All Services</span><span>Law Enforcement Services</span><span>Police Departments Services</span></div>

<section>
  <div class="abs card" style="top:1190px;left:180px;width:490px;height:350px"></div>
  <h2 class="abs display" style="top:1212px;left:205px;font-size:32px;line-height:42px">Police<br>Preparation</h2>
  <p class="abs para" style="top:1310px;left:205px;width:420px">Remote support built for patrol units, records rooms and dispatch desks, keeping every workstation secure, patched and ready for the next shift, day or night.</p>
  <div class="abs btn" style="top:1450px;left:205px">Read More</div>
  <div class="abs photo" style="top:1130px;left:660px;width:345px;height:430px" role="img" aria-label="Police officer in cap speaking on a phone"></div>
  <div class="abs dots" style="top:1540px;left:975px"></div>
</section>

<section>
  <svg class="abs" style="top:1610px;left:0" width="1200" height="850" viewBox="0 0 1200 850">
    <polygon points="0,60 170,0 1200,150 1200,850 0,850" fill="#CADEEF"/>
    <polygon points="0,90 170,25 1200,180 1200,690 0,690" fill="#0054AA"/>
  </svg>
  <h2 class="abs display about-title">About Us</h2>
  <p class="abs para about-text">We are a small team of IT specialists who serve law enforcement agencies, with help desk, backup and cyber defence tailored to them.</p>
  <div class="abs cjis-label">CJIS COMPLIANCE</div>
  <div class="abs card service" style="left:620px">
    <svg width="64" height="64" viewBox="0 0 64 64" fill="none" stroke="#1d1f24" stroke-width="2"><circle cx="32" cy="18" r="8"/><circle cx="14" cy="26" r="6"/><circle cx="50" cy="26" r="6"/><path d="M18 54v-8a14 14 0 0128 0v8M4 50v-4a10 10 0 0116-8M60 50v-4a10 10 0 00-16-8"/></svg>
    <span>Offer Remote<br>IT Support</span></div>
  <div class="abs card service" style="left:815px">
    <svg width="64" height="64" viewBox="0 0 64 64" fill="none" stroke="#1d1f24" stroke-width="2"><ellipse cx="28" cy="14" rx="18" ry="6"/><path d="M10 14v32c0 3 8 6 18 6M46 14v14M10 30c0 3 8 6 18 6"/><circle cx="46" cy="44" r="12"/><path d="M40 44l4 4 8-8"/></svg>
    <span>Backup / Recovery<br>Services</span></div>
  <div class="abs card service" style="left:1010px">
    <svg width="64" height="64" viewBox="0 0 64 64" fill="none" stroke="#1d1f24" stroke-width="2"><rect x="20" y="28" width="24" height="20" rx="2"/><path d="M25 28v-6a7 7 0 0114 0v6M32 36v6M6 16h10M6 32h8M6 48h10M58 16H48M58 32h-8M58 48H48"/></svg>
    <span>Cyber<br>Security</span></div>
  <div class="abs arrow-btn" style="left:620px"><svg width="10" height="10" viewBox="0 0 10 10"><path d="M7 1L3 5l4 4" stroke="#fff" stroke-width="2" fill="none"/></svg></div>
  <div class="abs arrow-btn" style="left:656px;background:#fff"><svg width="10" height="10" viewBox="0 0 10 10"><path d="M3 1l4 4-4 4" stroke="#0054AA" stroke-width="2" fill="none"/></svg></div>
  <div class="abs photo" style="top:2060px;left:0;width:610px;height:380px;background:linear-gradient(180deg,#9fb4c8,#4a5563 60%,#2b3036)" role="img" aria-label="Police patrol car parked in front of a city skyline"></div>
</section>

<section>
  <h2 class="abs display" style="top:2548px;left:0;width:1200px;text-align:center;font-size:40px">Follow Up</h2>
  <p class="abs para" style="top:2620px;left:200px;width:800px;text-align:center">After every ticket we check back with your department to confirm systems run smoothly, report what was fixed, and plan upgrades before issues reach the field. Regular reviews keep your records safe, your audits clean and your officers focused on duty.</p>
  <div class="abs" style="top:2760px;left:170px;width:500px;height:390px;background:var(--grey)"></div>
  <h2 class="abs display" style="top:2860px;left:225px;font-size:26px">Attorney Marcus</h2>
  <p class="abs para" style="top:2910px;left:225px;width:410px">Our legal advisor reviews every service agreement so agencies meet data handling rules and evidence chain standards without extra paperwork for staff.</p>
  <div class="abs btn" style="top:3070px;left:225px">Read More</div>
  <div class="abs photo" style="top:2752px;left:660px;width:350px;height:380px;background:linear-gradient(160deg,#9a8a78,#3a3430)" role="img" aria-label="Attorney in a suit reviewing documents at a desk"></div>
  <div class="abs dots" style="top:3140px;left:965px"></div>
</section>

<section>
  <h2 class="abs display" style="top:3320px;left:0;width:1200px;text-align:center;font-size:40px">Testimonials</h2>
  <div class="abs card quote" style="left:90px"><span class="avatar" role="img" aria-label="Portrait of client"></span><p>Hey, I just wanted to let you know how lucky our precinct felt to work with this team. Fast fixes.</p><div class="meta"><span>Nora Vale</span><span class="stars">★★★★</span></div></div>
  <div class="abs card quote" style="left:500px"><span class="avatar" role="img" aria-label="Portrait of client"></span><p>Their training and recovery plans got our records back online within hours after an outage.</p><div class="meta"><span>Peter Lind</span><span class="stars">★★★★</span></div></div>
  <div class="abs card quote" style="left:920px"><span class="avatar" role="img" aria-label="Portrait of client"></span><p>Honestly I was unsure at first, but they found risks we had missed for years.</p><div class="meta"><span>Owen Hale</span><span class="stars">★★★★</span></div></div>
</section>

<div class="abs photo" style="top:3700px;left:400px;width:400px;height:250px;background:linear-gradient(180deg,#ffffff 0%,#5c6470 45%,#1c1f26 100%)" role="img" aria-label="Group of police officers standing with arms crossed"></div>

<footer>
  <div class="abs footer"></div>
  <h2 class="abs display news-title">Newsletter</h2>
  <div class="abs news-form"><span>Enter your email address</span><b>SUBSCRIBE</b></div>
  <div class="abs" style="top:4228px;left:90px;width:110px;height:70px;background:#4a4f58"></div>
  <div class="abs col" style="left:350px"><h4>Quick Links</h4><ul><li>Services</li><li>About Us</li><li>Follow Up</li><li>CJIS Compliance</li><li>Contact Us</li></ul></div>
  <div class="abs col" style="left:535px"><h4>Company</h4><ul><li>Site Map</li><li>Terms &amp; Condition</li><li>Privacy Policy</li><li>FAQ's</li><li>Disclaimer</li></ul></div>
  <div class="abs col" style="left:730px;width:180px"><h4>Contact Info</h4><div>Fax<br>+00 (000) 00-0000</div><div style="margin-top:6px">Phone<br>+00 (000) 00-0000</div><div style="margin-top:6px">Location<br>1 Example Street, Suite 100</div></div>
  <div class="abs col" style="left:950px"><h4>Follow Us</h4><div class="social" style="display:flex;gap:10px"><span style="width:30px;height:30px;border-radius:50%;background:#3a3f48"></span><span style="width:30px;height:30px;border-radius:50%;background:#3a3f48"></span><span style="width:30px;height:30px;border-radius:50%;background:#3a3f48"></span></div></div>
  <div class="abs copy">Copyright 2021. All rights reserved.</div>
  <div class="abs" style="top:4440px;left:1134px;width:40px;height:40px;border-radius:50%;background:#fff;display:flex;align-items:center;justify-content:center"><svg width="12" height="12" viewBox="0 0 12 12"><path d="M2 8l4-4 4 4" stroke="#1c1f26" stroke-width="2" fill="none"/></svg></div>
</footer>

</body>
</html>
```